SnackNook!!! A Vending Machine Business Looking for an attractive website.

We are a vending machine business in Northern Michigan. We have changed our name and have rebranded our company. We would like an attractive website that shares who we are, what services we provide, the products we offer in our machines, along with a form businesses can fill out to see if they are a good fit for our company. I would like to have a Home Page, About SnackNook, Why Choose SnackNook?, Products & Services, Contact Us (With a Login Option), and a page with a questionnaire for thos interested in getting a FREE Vending Machine.

Target Market(s)

Businesses, Campgrounds, Schools, and many more in Northern Michigan

Industry/Entity Type

Vending Machines

Coding

Coded - Design and coding required

Number of Pages Required

5+ page

Requirements
Must have
• An inviting and enticing Home Page. I want to get my potential clients engaged in our website.
Nice to have
• Possibly background photos from Northern Michigan
Should not have
• A corporate feel. I do not want a boring website.

```html
<!DOCTYPE html>
<html lang="en">
<head>
<meta charset="utf-8">
<title>SnackNook – Crave. Vend. Repeat</title>
<link href="https://fonts.googleapis.com/css2?family=Lora:wght@600;700&family=Poppins:wght@400;500;600&display=swap" rel="stylesheet">
<style>
:root{
  --navy:#27215f;
  --navy-deep:#221c55;
  --green:#2f5a2a;
  --green-mid:#3a6431;
  --ink:#1a1a1a;
  --muted:#555;
  --white:#fff;
  --line:#c9c9c9;
}
*{margin:0;padding:0;box-sizing:border-box}
html,body{width:1200px;height:3849px;overflow:hidden}
body{font-family:"Poppins",sans-serif;color:var(--ink);background:var(--white);position:relative}
.abs{position:absolute}
.serif{font-family:"Lora",serif;font-weight:700}
.btn{position:absolute;display:flex;align-items:center;justify-content:center;color:var(--white);font-size:12px;font-weight:600;border-radius:4px}
.btn--navy{background:var(--navy)}
.btn--green{background:var(--green)}
.brand{font-family:"Poppins",sans-serif;font-weight:600;color:var(--navy);letter-spacing:-.5px}

/* header */
.site-header{position:absolute;top:0;left:0;width:1200px;height:85px;background:var(--white)}
.site-header .brand{position:absolute;left:142px;top:20px;font-size:34px}
.main-nav{position:absolute;top:33px;left:453px;display:flex;font-size:13px}
.main-nav span{position:absolute;white-space:nowrap}
.main-nav .active{color:var(--green);font-weight:600}

/* hero */
.hero{position:absolute;top:85px;left:0;width:1200px;height:528px;background:linear-gradient(90deg,#2c2d30 0%,#4a4a4c 35%,#d9d3cb 55%,#b9b3ad 75%,#3b3a52 100%)}
.hero__shade{position:absolute;inset:0;background:linear-gradient(90deg,rgba(0,0,0,.55) 0%,rgba(0,0,0,.2) 45%,rgba(0,0,0,0) 70%)}
.hero__title{position:absolute;left:142px;top:152px;color:var(--white);font-size:45px;font-weight:500;line-height:56px}
.hero__sub{position:absolute;left:142px;top:277px;color:var(--white);font-size:21px;font-weight:500}

/* about */
.about__photo{position:absolute;left:159px;top:696px;width:412px;height:412px;border-radius:50%;background:linear-gradient(160deg,#8d8d8a,#d8d4cc 50%,#6a6f78)}
.about__ring{position:absolute;left:151px;top:690px;width:420px;height:420px;border-radius:50%;border:10px solid var(--green);border-right-color:transparent;border-bottom-color:transparent;transform:rotate(-20deg)}
.about__label{position:absolute;left:643px;top:750px;font-size:18px;color:var(--green)}
.about .brand{position:absolute;left:638px;top:794px;font-size:38px}
.about__text{position:absolute;left:638px;top:864px;width:420px;font-size:11.5px;line-height:23px;color:#333;letter-spacing:.3px}
.about__text b{font-weight:600;color:var(--ink)}

/* machines */
.machines{position:absolute;top:1180px;left:0;width:1200px;height:753px}
.machine{position:absolute;top:0;width:600px;height:753px;color:var(--white);text-align:center}
.machine--navy{left:0;background:var(--navy-deep)}
.machine--green{left:600px;background:var(--green-mid)}
.machine__img{position:absolute;top:90px;left:251px;width:245px;height:418px;border-radius:3px;background:linear-gradient(180deg,#3a3d44,#9aa0a8 40%,#2d2f35)}
.machine__title{position:absolute;top:518px;left:0;width:100%;font-size:27px}
.machine__text{position:absolute;top:558px;left:170px;width:420px;font-size:11.5px;line-height:23px;margin-left:-50px;width:460px;left:120px}

/* why */
.why__heading{position:absolute;top:2012px;left:0;width:1200px;text-align:center;font-size:39px;color:var(--ink)}
.why__heading em{font-style:normal;color:var(--green)}
.why__heading em i{font-style:normal;color:var(--navy)}
.why__circle{position:absolute;left:408px;top:2102px;width:374px;height:374px;border-radius:50%;border:2px dashed var(--line)}
.why__core{position:absolute;left:464px;top:2158px;width:262px;height:262px;border-radius:50%;background:var(--white);box-shadow:0 0 18px rgba(0,0,0,.12);display:flex;align-items:center;justify-content:center}
.why__core .brand{font-size:36px}
.icon-dot{position:absolute;width:78px;height:78px;border-radius:50%;display:flex;align-items:center;justify-content:center}
.icon-dot--navy{background:var(--navy)}
.icon-dot--green{background:var(--green)}
.feature{position:absolute;width:228px}
.feature h3{font-family:"Lora",serif;font-weight:700;font-size:16px;line-height:21px;margin-bottom:8px}
.feature p{font-size:10px;line-height:19px;color:var(--muted);letter-spacing:.4px}
.feature--left{text-align:right;left:145px}
.feature--right{left:826px}

/* testimonials */
.testimonials{position:absolute;top:2585px;left:0;width:1200px;height:500px;background:var(--green)}
.testimonials h2{position:absolute;top:92px;width:100%;text-align:center;color:var(--white);font-size:39px}
.quote-card{position:absolute;top:186px;width:444px;height:160px;background:var(--white);border-radius:4px}
.quote-card::after{content:"";position:absolute;left:74px;bottom:-12px;border:8px solid transparent;border-top:12px solid var(--white);border-bottom:0}
.quote-card p{position:absolute;left:76px;top:40px;width:345px;font-size:11.5px;line-height:22px;color:#222}
.quote-mark{position:absolute;font-family:"Lora",serif;font-size:80px;line-height:1;color:#a9a6be}
.client{position:absolute;top:366px;display:flex;align-items:center;gap:12px;color:var(--white);font-family:"Lora",serif;font-weight:700;font-size:16px}
.avatar{width:52px;height:52px;border-radius:50%;background:#b9b2aa;border:3px solid var(--white)}
.arrow{position:absolute;width:36px;height:36px;border-radius:50%;display:flex;align-items:center;justify-content:center}

/* cta */
.cta h2{position:absolute;top:3170px;width:1200px;text-align:center;font-size:39px;line-height:51px}
.cta h2 em{font-style:normal;color:var(--green)}
.cta h2 em i{font-style:normal;color:var(--navy)}
.cta p{position:absolute;top:3280px;width:1200px;text-align:center;font-size:14px;line-height:27px;font-weight:500}

/* footer */
.site-footer{position:absolute;top:3476px;left:0;width:1200px;height:319px;background:var(--navy-deep);color:var(--white)}
.site-footer h4{position:absolute;font-family:"Lora",serif;font-weight:700;font-size:18px}
.quick-links{position:absolute;left:143px;top:124px;list-style:none;font-size:12px}
.quick-links li{height:30px;display:flex;gap:9px;align-items:flex-start}
.quick-links li::before{content:"";margin-top:5px;border:4px solid transparent;border-left:5px solid var(--white);border-right:0}
.site-footer .brand{position:absolute;left:0;width:1200px;text-align:center;top:132px;font-size:58px;color:var(--white)}
.socials{position:absolute;top:224px;left:518px;display:flex;gap:7px}
.socials span{width:28px;height:28px;border-radius:50%;border:1.5px solid var(--white)}
.contact-row{position:absolute;left:868px;display:flex;gap:12px;font-size:12px;line-height:18px}
.copyright{position:absolute;top:3795px;left:0;width:1200px;height:54px;background:var(--green);color:var(--white);display:flex;align-items:center;justify-content:center;font-family:"Lora",serif;font-weight:600;font-size:13px}
</style>
</head>
<body>

<header class="site-header">
  <div class="brand">SnackNook</div>
  <nav class="main-nav">
    <span class="active" style="left:0">Home</span>
    <span style="left:65px">About</span>
    <span style="left:130px">Why Choose Us</span>
    <span style="left:257px">Products &amp; Services</span>
    <span style="left:408px">Contact Us</span>
  </nav>
  <div class="btn btn--navy" style="left:958px;top:25px;width:100px;height:35px;font-weight:500">Log In</div>
</header>

<section class="hero">
  <div class="abs" role="img" aria-label="Office lounge with two stocked snack vending machines" style="inset:0"></div>
  <div class="hero__shade"></div>
  <h1 class="hero__title">SnackNook :<br>Crave. Vend. Repeat</h1>
  <p class="hero__sub">Elevating Snacking, One Vend at a Time</p>
  <div class="btn btn--navy" style="left:142px;top:330px;width:102px;height:32px;font-weight:500">Contact Us</div>
</section>

<section class="about">
  <div class="about__ring"></div>
  <div class="about__photo" role="img" aria-label="Customer choosing a snack from a vending machine"></div>
  <h2 class="about__label serif">About</h2>
  <div class="brand">SnackNook</div>
  <p class="about__text">At SnackNook, we don't just vend snacks—we curate cravings. Our customized vending solutions bring flavor, convenience, and community to Northern Michigan. Whether you're reaching for a <b>mid-morning snack</b>, a <b>refreshing beverage</b>, or a <b>satisfying breakfast burrito</b>, SnackNook delivers delight with every bite</p>
  <div class="btn btn--navy" style="left:638px;top:996px;width:123px;height:35px">Contact Us</div>
</section>

<section class="machines">
  <article class="machine machine--navy">
    <div class="machine__img" role="img" aria-label="Snack vending machine with glass front"></div>
    <h3 class="machine__title serif">Vending Machine - 1</h3>
    <p class="machine__text">Lorem ipsum dolor sit amet, consectetuer adipiscing elit, sed diam nonummy nibh euismod tincidunt ut laoreet dolore magna aliquam erat volutpat. Ut wisi enim ad minim veniam.</p>
    <div class="btn btn--green" style="left:309px;top:643px;width:123px;height:34px">View Details</div>
  </article>
  <article class="machine machine--green">
    <div class="machine__img" style="left:124px;top:90px;width:212px" role="img" aria-label="Combo snack and drink vending machine"></div>
    <h3 class="machine__title serif">Vending Machine - 2</h3>
    <p class="machine__text">Lorem ipsum dolor sit amet, consectetuer adipiscing elit, sed diam nonummy nibh euismod tincidunt ut laoreet dolore magna aliquam erat volutpat. Ut wisi enim ad minim veniam.</p>
    <div class="btn btn--navy" style="left:167px;top:645px;width:123px;height:34px">View Details</div>
  </article>
</section>

<section class="why">
  <h2 class="why__heading serif">Why Choose <em>Snack<i>Nook</i></em></h2>
  <div class="why__circle"></div>
  <div class="why__core"><span class="brand">SnackNook</span></div>

  <div class="icon-dot icon-dot--navy" style="left:394px;top:2150px">
    <svg width="38" height="38" viewBox="0 0 24 24" fill="none" stroke="#fff" stroke-width="1.4"><path d="M12 22s-7-7-7-12a7 7 0 0 1 14 0c0 5-7 12-7 12z"/><path d="M12 13.5l-2.6-2.5a1.6 1.6 0 0 1 2.6-2 1.6 1.6 0 0 1 2.6 2z"/></svg>
  </div>
  <div class="icon-dot icon-dot--green" style="left:721px;top:2150px">
    <svg width="38" height="38" viewBox="0 0 24 24" fill="none" stroke="#fff" stroke-width="1.4"><path d="M7 11v9H4v-9zM7 19h9l3-6v-2h-6l1-4-2-1-5 5"/></svg>
  </div>
  <div class="icon-dot icon-dot--green" style="left:391px;top:2351px">
    <svg width="38" height="38" viewBox="0 0 24 24" fill="none" stroke="#fff" stroke-width="1.4"><circle cx="9" cy="9" r="6"/><circle cx="15" cy="15" r="6"/></svg>
  </div>
  <div class="icon-dot icon-dot--navy" style="left:720px;top:2351px">
    <svg width="38" height="38" viewBox="0 0 24 24" fill="none" stroke="#fff" stroke-width="1.4"><path d="M4 20h16M6 20v-5M10 20v-8M14 20v-6M18 20v-10M5 11l5-4 4 3 6-6"/></svg>
  </div>

  <div class="feature feature--left" style="top:2124px">
    <h3>Local Love</h3>
    <p>We celebrate the heart of Michigan by partnering with local legends. Say hello to Pine Ridge Jerky and North Shore Potato Chips—our hometown heroes. Their flavorsdance on your taste buds, and we're thrilled to bring them straight to your workplace.</p>
  </div>
  <div class="feature feature--left" style="top:2332px">
    <h3>Unleash Your Cravings</h3>
    <p>SnackNook isn't bound by corporate ties. We're the rebels of the vending world. Craving a bag of crispy, kettle-cooked chips? Done. Hankering for jerky that packs a punch? We've got you covered. Our machines are like treasure chests, waiting for you to unlock flavor magic</p>
  </div>
  <div class="feature feature--right" style="top:2124px">
    <h3>Quality Meets Convenience</h3>
    <p>Imagine this: You're mid-meeting, and your stomach growls. Fear not! SnackNook's machines offer top-notch snacks and beverages. It's like having a mini food festival at your fingertips</p>
  </div>
  <div class="feature feature--right" style="top:2333px">
    <h3>Pandemic-Proof &amp;<br>Recession-Ready</h3>
    <p>Life throws curveballs, but SnackNook stands strong. Our vending machines are the unsung heroes of resilience. Rain or shine, they're there, serving up joy</p>
  </div>
</section>

<section class="testimonials">
  <h2 class="serif">What Our Clients Say</h2>
  <div class="arrow" style="left:84px;top:254px;border:1.5px solid #cfd8cc">
    <svg width="18" height="18" viewBox="0 0 24 24" fill="none" stroke="#fff" stroke-width="2"><path d="M19 12H5M11 6l-6 6 6 6"/></svg>
  </div>
  <div class="arrow" style="left:1080px;top:240px;background:var(--navy)">
    <svg width="18" height="18" viewBox="0 0 24 24" fill="none" stroke="#fff" stroke-width="2"><path d="M5 12h14M13 6l6 6-6 6"/></svg>
  </div>
  <div class="quote-card" style="left:142px">
    <span class="quote-mark" style="left:20px;top:10px">“</span>
    <p>Lorem ipsum dolor sit amet, consectetur adipiscing elit. Maecenas pretium tortor, non consectetur nulla. Aenean dignissim sit amet metus at pretium. Integer sed lectus vel velit accumsan semper euac...</p>
    <span class="quote-mark" style="left:264px;top:92px">”</span>
  </div>
  <div class="quote-card" style="left:614px">
    <span class="quote-mark" style="left:20px;top:10px">“</span>
    <p>Lorem ipsum dolor sit amet, consectetur adipiscing elit. Maecenas pretium tortor, non consectetur nulla. Aenean dignissim sit amet metus at pretium. Integer sed lectus vel velit accumsan semper euac...</p>
    <span class="quote-mark" style="left:264px;top:92px">”</span>
  </div>
  <div class="client" style="left:195px"><span class="avatar" role="img" aria-label="Client portrait"></span>Dale Monroe</div>
  <div class="client" style="left:668px"><span class="avatar" role="img" aria-label="Client portrait"></span>Tessa Morgan</div>
</section>

<section class="cta">
  <h2 class="serif">Ready To Experience The<br><em>Snack<i>Nook</i></em> Difference?</h2>
  <p>Sign up now and let's connect. Taste the future of snacking firsthand! Contact us today<br>and explore how our vending magic can elevate your space.</p>
  <div class="btn btn--green" style="left:544px;top:3350px;width:112px;height:37px">Contact Us</div>
</section>

<footer class="site-footer">
  <h4 style="left:143px;top:80px">Quick Links</h4>
  <ul class="quick-links">
    <li>Home</li>
    <li>About Us</li>
    <li>Why Choose SnackNook</li>
    <li>Product and Services</li>
    <li>Contact Us</li>
  </ul>
  <div class="brand">SnackNook</div>
  <div class="socials" aria-label="Social links"><span></span><span></span><span></span><span></span></div>
  <h4 style="left:868px;top:80px">Contact Details</h4>
  <div class="contact-row" style="top:122px">
    <svg width="26" height="26" viewBox="0 0 24 24" fill="none" stroke="#fff" stroke-width="1.3"><circle cx="12" cy="12" r="9"/><path d="M3 12h18M12 3c3 3 3 15 0 18M12 3c-3 3-3 15 0 18"/></svg>
    <span>123, Building Name, Street<br>City, State XY 123456</span>
  </div>
  <div class="contact-row" style="top:176px">
    <svg width="26" height="26" viewBox="0 0 24 24" fill="none" stroke="#fff" stroke-width="1.3"><path d="M5 3h4l2 5-2.5 1.5a11 11 0 0 0 6 6L16 13l5 2v4a2 2 0 0 1-2 2A16 16 0 0 1 3 5a2 2 0 0 1 2-2z"/></svg>
    <span>PHONE<br>123-456-7890</span>
  </div>
  <div class="contact-row" style="top:230px">
    <svg width="26" height="26" viewBox="0 0 24 24" fill="none" stroke="#fff" stroke-width="1.3"><rect x="3" y="5" width="18" height="14" rx="1"/><path d="M3 6l9 7 9-7"/></svg>
    <span>EMAIL<br>info@snacknook.com</span>
  </div>
</footer>
<div class="copyright">© 2024 SnackNook. all rights reserved.</div>

</body>
</html>
```